Flyer für KFZ-Gutachter
Zielgruppe
NFZ und KFZ Gutachten. Firma ist neu gegründet und Flyer wird benötigt um sich bei Werkstätten, Versicherungen und Privatkunden vorzustellen.
Aufgabenstellung
Es soll elegant, klassisch sein und angelehnt sein an meine Website https://www.holvarentis.de/ Handynummer 0157 - 62830417 bitte einpflegen. Außerdem sollten die Logos des Bundesverbandes und der Zertifizierung mit im Flyer eingebunden werden. Diese lade ich hoch. Auch das korrekte Logo lade ich hoch.

```html
<!DOCTYPE html>
<html lang="de">
<head>
<meta charset="utf-8">
<title>Holvarentis Stuttgart – Flyer</title>
<link href="https://fonts.googleapis.com/css2?family=Noto+Serif:wght@300;400;500;600;700&display=swap" rel="stylesheet">
<style>
  :root{
    --page:#f0f0f0;
    --paper:#e8e8e8;
    --photo-a:#646a66;
    --photo-b:#8b918d;
    --shirt:#8fa9cc;
    --hall-a:#0e0e0e;
    --hall-b:#4a4a4a;
    --ink:#1d1d1d;
    --band:#1e1e1e;
    --white:#ffffff;
    --muted:#6a6a6a;
    --badge:#2f8fc4;
    --badge-b:#8fb6d4;
    --accent:#c8102e;
  }
  html,body{margin:0;padding:0;width:1080px;height:1200px;overflow:hidden;background:var(--page);}
  body{font-family:"Noto Serif",Georgia,serif;color:var(--ink);}
  .stage{position:relative;width:1080px;height:1200px;}

  .flyer{
    position:absolute;top:247px;width:624px;height:882px;
    transform:scale(.8);transform-origin:0 0;
    background:var(--paper);overflow:hidden;
    box-shadow:0 2px 10px rgba(0,0,0,.12);
  }
  .flyer--light{left:24px;}
  .flyer--dark{left:557px;}

  .hero{position:absolute;left:0;top:0;width:624px;height:720px;}
  .band{position:absolute;left:0;bottom:0;width:624px;height:162px;background:var(--band);}

  /* light variant */
  .brand{position:absolute;right:24px;top:118px;text-align:center;color:var(--white);}
  .brand-name{font-size:24px;font-weight:500;letter-spacing:1px;line-height:1;display:flex;align-items:center;justify-content:center;gap:8px;}
  .brand-name::before{content:"";width:13px;height:13px;background:var(--white);display:inline-block;}
  .brand-city{font-size:9px;font-weight:500;letter-spacing:8px;margin-top:6px;padding-left:22px;}
  .headline{position:absolute;left:0;width:550px;top:318px;text-align:right;color:var(--white);
    font-size:38px;font-weight:400;margin:0;letter-spacing:-.3px;}
  .headline-rule{position:absolute;left:372px;top:382px;width:178px;height:1px;background:rgba(255,255,255,.8);}
  .subline{position:absolute;right:74px;top:405px;text-align:right;color:rgba(255,255,255,.85);
    font-size:19px;font-weight:300;line-height:24px;margin:0;}

  .service{position:absolute;background:var(--white);text-align:center;padding:0 12px;box-sizing:border-box;}
  .service svg{display:block;margin:0 auto;}
  .service h3{font-size:11.5px;font-weight:500;margin:22px 0 0;}
  .service .rule{width:60px;height:1px;background:var(--ink);margin:9px auto 14px;}
  .service p{font-size:7.4px;line-height:9.4px;color:var(--muted);margin:0;text-align:left;}
  .s1{left:80px;top:510px;width:142px;height:225px;padding-top:40px;}
  .s2{left:241px;top:497px;width:143px;height:251px;padding-top:53px;}
  .s3{left:406px;top:510px;width:143px;height:225px;padding-top:40px;}

  /* shared footer */
  .phone{position:absolute;left:45px;top:770px;width:210px;height:40px;background:var(--white);
    display:flex;align-items:center;gap:12px;padding-left:14px;box-sizing:border-box;font-size:19px;color:var(--ink);white-space:nowrap;}
  .address{position:absolute;left:45px;top:818px;color:#d8d8d8;font-size:15px;font-weight:300;margin:0;}
  .web{position:absolute;left:46px;top:846px;color:#d0d0d0;font-size:8px;letter-spacing:5.2px;margin:0;}
  .credentials{position:absolute;left:368px;top:783px;width:256px;height:57px;background:var(--white);
    display:flex;align-items:center;gap:8px;padding-left:28px;box-sizing:border-box;}
  .seal{width:34px;height:34px;border-radius:50%;background:var(--badge);}
  .seal.wide{width:50px;height:32px;background:var(--badge-b);}
  .expert{border-left:2px solid var(--accent);padding-left:7px;margin-left:12px;}
  .expert strong{display:block;font-size:8.5px;font-weight:500;}
  .expert small{display:block;font-size:4px;line-height:5px;color:var(--muted);width:62px;}

  /* dark variant */
  .logo-block{position:absolute;left:191px;top:0;width:249px;height:216px;background:var(--band);color:var(--white);text-align:center;}
  .logo-block .brand-name{font-size:24px;margin-top:128px;}
  .logo-block .brand-city{font-size:10px;margin-top:8px;padding-left:8px;}
  .dark-title{position:absolute;left:0;width:624px;top:252px;text-align:center;color:var(--white);font-size:31px;font-weight:500;margin:0;}
  .dark-rule{position:absolute;left:237px;top:305px;width:150px;height:1px;background:rgba(255,255,255,.7);}
  .dark-sub{position:absolute;left:0;width:624px;top:325px;text-align:center;color:rgba(255,255,255,.88);font-size:15px;font-weight:300;margin:0;}
  .info{position:absolute;top:373px;width:150px;height:255px;background:var(--white);padding:18px 10px 0 12px;box-sizing:border-box;}
  .info--services{left:155px;}
  .info--reasons{left:320px;}
  .info h3{font-size:11.5px;font-weight:500;margin:0;text-align:center;}
  .info .rule{width:60px;height:1px;background:var(--ink);margin:8px auto 14px;}
  .info ul{list-style:none;margin:0;padding:0;}
  .info li{font-size:7px;line-height:8.6px;color:var(--muted);margin-bottom:10px;}
  .info li b{display:block;color:var(--ink);font-weight:600;}
  .tagline{position:absolute;left:0;width:610px;top:657px;text-align:center;color:var(--white);font-size:10px;line-height:13px;margin:0;}
  .tagline b{font-weight:700;}
  .contact-call{position:absolute;left:45px;top:734px;color:var(--white);font-size:15.5px;margin:0;white-space:nowrap;}
  .contact-call b{font-weight:700;}
</style>
</head>
<body>
<div class="stage">

  <article class="flyer flyer--light">
    <svg class="hero" viewBox="0 0 624 720" role="img" aria-label="Foto zweier Gutachter in hellblauen Hemden vor grauem Hintergrund">
      <defs>
        <linearGradient id="heroTone" x1="0" y1="0" x2="1" y2="1">
          <stop offset="0" stop-color="var(--photo-a)"/>
          <stop offset="1" stop-color="var(--photo-b)"/>
        </linearGradient>
      </defs>
      <polygon points="0,67 624,24 624,505 0,548" fill="url(#heroTone)"/>
      <polygon points="75,270 430,240 470,512 70,545" fill="var(--shirt)" opacity=".6"/>
    </svg>
    <div class="band"></div>

    <div class="brand">
      <div class="brand-name">HOLVARENTIS</div>
      <div class="brand-city">STUTTGART</div>
    </div>

    <h1 class="headline">Ihr Experte für Gutachten</h1>
    <div class="headline-rule"></div>
    <p class="subline">Präzise Bewertungen<br>für Ihre Bedürfnisse</p>

    <section class="service s1">
      <svg width="30" height="30" viewBox="0 0 30 30" aria-hidden="true">
        <polygon points="10,2 12,8 18,6 14,11 19,14 12,14" fill="var(--ink)"/>
        <rect x="2" y="14" width="11" height="10" rx="2" fill="var(--ink)"/>
        <rect x="15" y="15" width="13" height="9" rx="2" fill="var(--ink)"/>
        <circle cx="6" cy="25" r="2.5" fill="var(--white)" stroke="var(--ink)"/>
        <circle cx="24" cy="25" r="2.5" fill="var(--white)" stroke="var(--ink)"/>
      </svg>
      <h3>Unfallgutachten</h3>
      <div class="rule"></div>
      <p>Wir erstellen detaillierte Unfall­gutachten, die Ihnen bei der Schadensregulierung helfen und für Versicherungen präzise nachvollziehbar sind.</p>
    </section>

    <section class="service s2">
      <svg width="30" height="26" viewBox="0 0 30 26" aria-hidden="true">
        <path d="M6 4h18l4 9v9h-4v-3H6v3H2v-9z" fill="var(--ink)"/>
        <rect x="8" y="7" width="14" height="5" fill="var(--white)"/>
        <circle cx="7" cy="15" r="1.8" fill="var(--white)"/>
        <circle cx="23" cy="15" r="1.8" fill="var(--white)"/>
      </svg>
      <h3>Wertgutachten</h3>
      <div class="rule"></div>
      <p>Erhalten Sie fundierte Wertgut­achten, die Ihnen bei Kaufent­scheidungen oder bei der Schadenregulierung nützlich sein können.</p>
    </section>

    <section class="service s3">
      <svg width="30" height="30" viewBox="0 0 30 30" aria-hidden="true">
        <g stroke="var(--ink)" stroke-width="1.4">
          <line x1="3" y1="3" x2="9" y2="9"/><line x1="7" y1="2" x2="13" y2="8"/><line x1="2" y1="8" x2="8" y2="13"/>
        </g>
        <path d="M12 14h12l4 6v7H10v-7z" fill="var(--ink)"/>
        <rect x="14" y="16" width="9" height="4" fill="var(--white)"/>
      </svg>
      <h3>Schadensgutachten</h3>
      <div class="rule"></div>
      <p>Präzise Schadensgutachten, die alle relevanten Informationen enthalten und die rechtlichen Anforderungen erfüllen.</p>
    </section>

    <div class="phone">
      <svg width="17" height="17" viewBox="0 0 24 24" aria-hidden="true">
        <path d="M6.6 10.8a15.1 15.1 0 0 0 6.6 6.6l2.2-2.2c.3-.3.7-.4 1-.2 1.1.4 2.3.6 3.6.6.6 0 1 .4 1 1V20c0 .6-.4 1-1 1A17 17 0 0 1 3 4c0-.6.4-1 1-1h3.5c.6 0 1 .4 1 1 0 1.3.2 2.5.6 3.6.1.3 0 .7-.2 1z" fill="var(--ink)"/>
      </svg>
      <span>0157 628 304 17</span>
    </div>
    <p class="address">Talgasse 18 — 71638 Ludwigsburg</p>
    <p class="web">WWW.HOLVARENTIS.DE</p>

    <div class="credentials">
      <div class="seal" role="img" aria-label="Zertifizierungssiegel"></div>
      <div class="seal wide" role="img" aria-label="Verbandssiegel"></div>
      <div class="expert">
        <strong>Armin Keldor</strong>
        <small>Geprüfter Sachverständiger für Fahrzeugschäden und Bewertung</small>
      </div>
    </div>
  </article>

  <article class="flyer flyer--dark">
    <svg class="hero" viewBox="0 0 624 720" role="img" aria-label="Schwarzweißfoto einer weiten, dunklen Halle mit Säulen und glänzendem Boden">
      <defs>
        <linearGradient id="hallTone" x1="0" y1="0" x2="1" y2="1">
          <stop offset="0" stop-color="var(--hall-a)"/>
          <stop offset=".55" stop-color="var(--hall-b)"/>
          <stop offset="1" stop-color="var(--hall-a)"/>
        </linearGradient>
      </defs>
      <polygon points="0,65 624,22 624,720 0,720" fill="url(#hallTone)"/>
    </svg>
    <div class="band"></div>

    <div class="logo-block">
      <div class="brand-name">HOLVARENTIS</div>
      <div class="brand-city">STUTTGART</div>
    </div>

    <h1 class="dark-title">Holvarentis Stuttgart</h1>
    <div class="dark-rule"></div>
    <p class="dark-sub">Ihr Experte für Fahrzeugbewertungen</p>

    <section class="info info--services">
      <h3>Unsere Leistungen</h3>
      <div class="rule"></div>
      <ul>
        <li><b>✓ Schaden- und Unfallgutachten</b>Präzise Bewertung nach Unfällen</li>
        <li><b>✓ Wertgutachten</b>Ermittlung des Fahrzeugwerts</li>
        <li><b>✓ Fahrzeugbewertung &amp; -zustand</b>Transparente Einschätzung für Kauf, Verkauf &amp; Leasing</li>
        <li><b>✓ Technische Untersuchungen</b>Begutachtung von Schäden, Defekten &amp; Mängeln</li>
        <li><b>✓ Fuhrpark-, Versicherungs- &amp; Anwaltsgutachten</b>Detaillierte und objektive Analysen</li>
      </ul>
    </section>

    <section class="info info--reasons">
      <h3>Warum wir?</h3>
      <div class="rule"></div>
      <ul>
        <li><b>✓ Unabhängig &amp; objektiv</b>Keine Interessenkonflikte</li>
        <li><b>✓ 15 Jahre Erfahrung</b>Experten in NFZ- &amp; KFZ-Technik</li>
        <li><b>✓ Jung &amp; innovativ</b>Moderne Lösungen für die Branche</li>
        <li><b>✓ Schnell &amp; effizient</b>Rasche Schadensbewertung</li>
        <li><b>✓ Kundenzufriedenheit</b>Maßgeschneiderte Lösungen</li>
      </ul>
    </section>

    <p class="tagline"><b>Holvarentis Stuttgart</b> – Vertrauen Sie auf Erfahrung &amp; Innovation!<br>Ihr kompetenter Partner in Stuttgart</p>

    <p class="contact-call"><b>Kontaktieren</b> Sie uns für eine <b>Beratung</b> oder <b>Terminvereinbarung!</b></p>

    <div class="phone">
      <svg width="17" height="17" viewBox="0 0 24 24" aria-hidden="true">
        <path d="M6.6 10.8a15.1 15.1 0 0 0 6.6 6.6l2.2-2.2c.3-.3.7-.4 1-.2 1.1.4 2.3.6 3.6.6.6 0 1 .4 1 1V20c0 .6-.4 1-1 1A17 17 0 0 1 3 4c0-.6.4-1 1-1h3.5c.6 0 1 .4 1 1 0 1.3.2 2.5.6 3.6.1.3 0 .7-.2 1z" fill="var(--ink)"/>
      </svg>
      <span>0157 628 304 17</span>
    </div>
    <p class="address">Talgasse 18 — 71638 Ludwigsburg</p>
    <p class="web">WWW.HOLVARENTIS.DE</p>

    <div class="credentials">
      <div class="seal" role="img" aria-label="Zertifizierungssiegel"></div>
      <div class="seal wide" role="img" aria-label="Verbandssiegel"></div>
      <div class="expert">
        <strong>Armin Keldor</strong>
        <small>Geprüfter Sachverständiger für Fahrzeugschäden und Bewertung</small>
      </div>
    </div>
  </article>

</div>
</body>
</html>
```